Gold Finch Print and Mailing Services

We are looking for a website layout design for a direct print and mailing company which prints graphics, post cards, letters, does mailing and more.

Please see attached logo, as it will be used to match color scheme of website.

Current website:
www.goldfinchprintpost.example

Websites we like:
https://velmorepress.example

Target Market(s)

Businesses / Media

Number of Pages Required

3 page

Font styles to use
Sans Serif

Requirements
Must have
• Color scheme to match logo

```html
<!DOCTYPE html>
<html lang="en">
<head>
<meta charset="utf-8">
<title>Gold Finch Print and Mailing Services</title>
<link rel="stylesheet" href="https://fonts.googleapis.com/css2?family=Arimo:wght@400;700&family=Courgette&family=Montserrat:wght@400;700&family=Raleway:wght@400;500&display=swap">
<style>
:root{
  --pink:#dc3491;
  --lime:#c9d400;
  --yellow:#d6e21a;
  --blue:#0b5a9e;
  --navy:#12467f;
  --ink:#333;
  --muted:#555;
  --dark:#1b1b1b;
  --white:#fff;
}
*{box-sizing:border-box;margin:0;padding:0}
html,body{width:1200px;height:3442px;overflow:hidden}
body{font-family:"Arimo",Arial,sans-serif;color:var(--ink);background:var(--white);position:relative}
section,header,footer{position:absolute;left:0;width:1200px}

/* header */
.site-header{top:0;height:105px;background:var(--white)}
.brand{position:absolute;left:87px;top:30px;display:flex;align-items:center;gap:10px;font-family:"Raleway",sans-serif;font-weight:500;font-size:24px;color:var(--navy)}
.brand-dot{width:34px;height:34px;border-radius:50%;background:var(--navy)}
.main-nav a{position:absolute;top:44px;font-size:17px;color:#444;text-decoration:none}
.phone-btn{position:absolute;left:957px;top:32px;width:167px;height:46px;border-radius:23px;background:var(--blue);color:var(--white);font-size:19px;display:flex;align-items:center;justify-content:center;gap:10px}
.phone-btn .ico{width:24px;height:24px;border-radius:50%;background:var(--yellow);display:flex;align-items:center;justify-content:center}

/* hero */
.hero{top:105px;height:572px;background:linear-gradient(120deg,#9a8e7a 0%,#c9bfa8 35%,#e8e2d3 55%,#a89a78 80%,#6d6653 100%)}
.hero h1{position:absolute;top:225px;width:100%;text-align:center;font-family:"Montserrat",sans-serif;font-weight:700;font-size:56px;line-height:64px;color:var(--white);text-shadow:0 2px 6px rgba(0,0,0,.4)}

/* product tiles */
.tiles{top:677px;height:367px;display:flex}
.tile{width:400px;height:367px;text-align:center;color:var(--white);padding-top:48px}
.tile h2{font-family:"Courgette",cursive;font-weight:400;font-size:34px;margin-bottom:22px}
.tile p{width:300px;margin:0 auto;font-size:14.5px;line-height:26px}
.tile-pink{background:var(--pink)}
.tile-lime{background:var(--lime);color:#222}
.tile-lime p{color:#5d6200}
.tile-blue{background:var(--blue)}
.outline-btn{display:inline-block;margin-top:34px;width:147px;height:52px;line-height:50px;border:1px solid currentColor;font-size:16px;color:inherit}

/* about */
.about{top:1044px;height:417px}
.about h2{position:absolute;left:80px;top:56px;font-family:"Raleway",sans-serif;font-weight:400;font-size:40px;color:var(--blue)}
.about h2 span,.services h2 span{color:var(--pink)}
.about p{position:absolute;left:78px;top:118px;width:560px;font-size:14.5px;line-height:26px;color:var(--muted)}
.solid-btn{position:absolute;background:var(--pink);color:var(--white);font-size:17px;display:flex;align-items:center;justify-content:center}
.about .solid-btn{left:78px;top:298px;width:145px;height:55px}
.about-photo{position:absolute;left:684px;top:62px;width:438px;height:291px;background:linear-gradient(135deg,#e8336d 0%,#f3c623 30%,#56c2d8 55%,#2c2f8f 80%,#eaeaea 100%);border:2px solid #eee}

/* banner */
.banner{top:1461px;height:289px;background:linear-gradient(180deg,#3e4447 0%,#2d3234 60%,#1e2223 100%)}
.banner p{position:absolute;top:82px;width:100%;text-align:center;font-family:"Montserrat",sans-serif;font-size:36px;line-height:47px;color:var(--yellow)}

/* services */
.services{top:1750px;height:741px}
.services h2{position:absolute;top:58px;width:100%;text-align:center;font-family:"Raleway",sans-serif;font-weight:400;font-size:38px;color:var(--blue)}
.service-grid{position:absolute;left:78px;top:138px;width:1044px;display:grid;grid-template-columns:repeat(4,255px);column-gap:8px;row-gap:46px}
.service-card{height:245px;background:var(--white);box-shadow:0 2px 8px rgba(0,0,0,.25);padding:8px}
.service-card h3{height:72px;display:flex;align-items:center;justify-content:center;text-align:center;font-family:"Courgette",cursive;font-weight:400;font-size:21px;line-height:24px;color:var(--pink)}
.service-photo{height:157px}
.ph-a{background:linear-gradient(135deg,#f1f1f1,#c9c3bd 60%,#8e8a86)}
.ph-b{background:linear-gradient(135deg,#b7b2a9,#6f6a63 50%,#2e3a55)}
.ph-c{background:linear-gradient(135deg,#2a2a2a,#6b6b6b 50%,#d9c43a 75%,#2a7fc2)}
.ph-d{background:linear-gradient(135deg,#7a4a2e,#c24a3a 45%,#e9ddd0 80%)}
.ph-e{background:linear-gradient(135deg,#cfd5da,#8d97a3 50%,#40331f)}
.ph-f{background:linear-gradient(135deg,#f3e5ec,#e0477f 45%,#c9b28a 80%)}
.ph-g{background:linear-gradient(135deg,#efe7dc,#f08a2c 45%,#d4c4ad 85%)}
.service-more{height:245px;background:linear-gradient(135deg,#e060a8,#c9307f);position:relative;box-shadow:0 2px 8px rgba(0,0,0,.25)}
.service-more .outline-btn{position:absolute;left:61px;top:96px;margin:0;width:138px;color:var(--white);text-align:center}

/* contact */
.contact{top:2491px;height:503px;background:linear-gradient(180deg,#6c6c6c,#9a9a9a 45%,#7b7b7b)}
.contact h2{position:absolute;top:52px;width:100%;text-align:center;font-family:"Raleway",sans-serif;font-weight:400;font-size:40px;color:var(--yellow)}
.field{position:absolute;background:rgba(255,255,255,.55);font-size:13px;color:#555;padding:16px 18px}
.contact .solid-btn{left:528px;top:381px;width:144px;height:57px}

/* footer */
.site-footer{top:2994px;height:383px;background:var(--dark);color:#ddd}
.site-footer h4{position:absolute;top:62px;font-weight:400;font-size:22px;color:var(--yellow)}
.foot-nav{position:absolute;left:80px;top:120px;list-style:none;font-size:14px;line-height:31px;color:var(--white)}
.foot-nav li::before{content:"";display:inline-block;width:8px;height:8px;border-radius:50%;background:var(--white);margin-right:14px;vertical-align:middle}
.touch{position:absolute;left:273px;top:118px;width:270px;font-size:13.5px;line-height:22px;color:#ddd}
.touch-row{display:flex;gap:16px;margin-bottom:16px}
.touch-row svg{flex:none;margin-top:3px}
.touch strong{color:var(--white);letter-spacing:.5px}
.blog{position:absolute;left:560px;width:290px;display:flex;gap:22px}
.blog-thumb{width:88px;height:88px;background:linear-gradient(135deg,#e8e8e8,#9aa3ad 60%,#5b6570)}
.blog p{font-size:15px;line-height:24px;color:var(--white)}
.blog small{display:block;margin-top:10px;font-size:13px;color:#ccc}
.newsletter p{position:absolute;left:872px;top:128px;width:250px;font-size:13.5px;line-height:22px}
.email-box{position:absolute;left:872px;top:224px;width:232px;height:48px;border-radius:24px;background:var(--white);color:#666;font-size:13px;padding:16px 20px}
.email-go{position:absolute;right:-18px;top:0;width:84px;height:48px;border-radius:24px;background:var(--yellow);display:flex;align-items:center;justify-content:center}
.social{position:absolute;left:910px;top:294px;display:flex;gap:12px}
.social span{width:34px;height:34px;border-radius:50%;background:var(--yellow);border:2px solid #444}
.bottom-bar{position:absolute;left:0;top:3377px;width:1200px;height:65px;background:var(--pink);color:var(--white);font-size:13px}
.bottom-bar p{position:absolute;left:80px;top:24px}
.foot-brand{position:absolute;left:1021px;top:8px;width:101px;height:50px;background:var(--white);color:var(--navy);font-family:"Raleway",sans-serif;font-weight:500;font-size:15px;display:flex;align-items:center;justify-content:center}
</style>
</head>
<body>

<header class="site-header">
  <div class="brand"><span class="brand-dot"></span>Gold Finch</div>
  <nav class="main-nav">
    <a href="#" style="left:287px">Home</a>
    <a href="#" style="left:367px">About Us</a>
    <a href="#" style="left:466px">Services &amp; Print Products</a>
    <a href="#" style="left:690px">FAQ</a>
    <a href="#" style="left:755px">News</a>
    <a href="#" style="left:830px">Contact Us</a>
  </nav>
  <div class="phone-btn"><span class="ico"><svg width="13" height="13" viewBox="0 0 24 24"><path d="M6.6 10.8a15 15 0 006.6 6.6l2.2-2.2c.3-.3.7-.4 1-.2 1.1.4 2.3.6 3.6.6.6 0 1 .4 1 1V20c0 .6-.4 1-1 1A17 17 0 013 4c0-.6.4-1 1-1h3.5c.6 0 1 .4 1 1 0 1.3.2 2.5.6 3.6.1.3 0 .7-.2 1z" fill="#0b5a9e"/></svg></span>123 456 7890</div>
</header>

<section class="hero" role="img" aria-label="Photo of a smiling businesswoman in an office">
  <h1>Make A Professional First<br>Impression</h1>
</section>

<section class="tiles">
  <div class="tile tile-pink">
    <h2>Post Cards</h2>
    <p>Lorem Ipsum is simply dummy text of the printing and typesetting industry. Lorem Ipsum has been the industry's standard dummy text ever since the 1500s.</p>
    <span class="outline-btn">READ MORE</span>
  </div>
  <div class="tile tile-lime">
    <h2>Prints Graphics</h2>
    <p>Lorem Ipsum is simply dummy text of the printing and typesetting industry. Lorem Ipsum has been the industry's standard dummy text ever since the 1500s.</p>
    <span class="outline-btn">READ MORE</span>
  </div>
  <div class="tile tile-blue">
    <h2>Letters</h2>
    <p>Lorem Ipsum is simply dummy text of the printing and typesetting industry. Lorem Ipsum has been the industry's standard dummy text ever since the 1500s.</p>
    <span class="outline-btn">READ MORE</span>
  </div>
</section>

<section class="about">
  <h2>About <span>Us</span></h2>
  <p>Even in today's digital marketplace, mail continues to be one of the most effective forms of communication. Gold Finch's mastery of the complexities of managed mail gives our clients the assurance that their mailings will be handled in the most professional, cost-effective, and efficient way possible. That means rapid results without the worry. You'll always get the optimum postage rates with our help. We'll even provide affordable mailing lists with advanced demographic filters.</p>
  <span class="solid-btn">READ MORE</span>
  <div class="about-photo" role="img" aria-label="Colour print proofs with a loupe magnifier"></div>
</section>

<section class="banner" role="img" aria-label="Dark mountain landscape backdrop">
  <p>No Design?<br>No Problem Let Our Expert Designers<br>Help You</p>
</section>

<section class="services">
  <h2>Services <span>&amp; Print Products</span></h2>
  <div class="service-grid">
    <div class="service-card"><h3>Lettershop Services</h3><div class="service-photo ph-a" role="img" aria-label="Printed charts and documents on a desk"></div></div>
    <div class="service-card"><h3>Mail Sorting</h3><div class="service-photo ph-b" role="img" aria-label="Office staff at a printer"></div></div>
    <div class="service-card"><h3>Color Digital Printing</h3><div class="service-photo ph-c" role="img" aria-label="Ink cartridges in a colour printer"></div></div>
    <div class="service-card"><h3>Fulfillment Services</h3><div class="service-photo ph-d" role="img" aria-label="Holiday greeting cards"></div></div>
    <div class="service-card"><h3>Graphics Services</h3><div class="service-photo ph-e" role="img" aria-label="Photo prints held in hands"></div></div>
    <div class="service-card"><h3>Mail List &amp; Digital Mail</h3><div class="service-photo ph-f" role="img" aria-label="Person working at a computer"></div></div>
    <div class="service-card"><h3>Laser Printing</h3><div class="service-photo ph-g" role="img" aria-label="Printed photo album pages"></div></div>
    <div class="service-more" role="img" aria-label="Pink tinted photo behind view all button"><span class="outline-btn">VIEW ALL</span></div>
  </div>
</section>

<section class="contact" role="img" aria-label="Print shop with large format printer, greyscale">
  <h2>Contact Us</h2>
  <div class="field" style="left:282px;top:147px;width:312px;height:55px">Name :</div>
  <div class="field" style="left:603px;top:147px;width:315px;height:55px">Phone :</div>
  <div class="field" style="left:282px;top:216px;width:312px;height:55px">Email :</div>
  <div class="field" style="left:603px;top:216px;width:315px;height:55px">Company :</div>
  <div class="field" style="left:282px;top:280px;width:636px;height:90px">Message / Comments :</div>
  <span class="solid-btn">SUBMIT</span>
</section>

<footer class="site-footer">
  <h4 style="left:80px">Navigation</h4>
  <h4 style="left:273px">Get In Touch</h4>
  <h4 style="left:560px">Recent Blog</h4>
  <h4 style="left:872px">Newsletter</h4>

  <ul class="foot-nav">
    <li>Home</li><li>About</li><li>Services &amp; Product</li><li>FAQs</li><li>News</li><li>Contact</li>
  </ul>

  <div class="touch">
    <div class="touch-row"><svg width="14" height="18" viewBox="0 0 14 18"><path d="M7 0a7 7 0 00-7 7c0 5 7 11 7 11s7-6 7-11a7 7 0 00-7-7zm0 10a3 3 0 110-6 3 3 0 010 6z" fill="#fff"/></svg><div><strong>GOLD FINCH</strong><br>Lorem Ipsum is simply dummy printing and typesetting industry.</div></div>
    <div class="touch-row"><svg width="16" height="16" viewBox="0 0 24 24"><path d="M6.6 10.8a15 15 0 006.6 6.6l2.2-2.2c.3-.3.7-.4 1-.2 1.1.4 2.3.6 3.6.6.6 0 1 .4 1 1V20c0 .6-.4 1-1 1A17 17 0 013 4c0-.6.4-1 1-1h3.5c.6 0 1 .4 1 1 0 1.3.2 2.5.6 3.6.1.3 0 .7-.2 1z" fill="#fff"/></svg>(555) 014-2297</div>
    <div class="touch-row"><svg width="17" height="13" viewBox="0 0 17 13"><rect width="17" height="13" fill="#fff"/><path d="M0 0l8.5 7L17 0" stroke="#1b1b1b" stroke-width="1.5" fill="none"/></svg>info@goldfinchprint.example</div>
  </div>

  <div class="blog" style="top:120px"><div class="blog-thumb" role="img" aria-label="Blog thumbnail of people at a desk"></div><p>Lorem Ipsum simply dummy printing text<small>March , 21 2017</small></p></div>
  <div class="blog" style="top:234px"><div class="blog-thumb" role="img" aria-label="Blog thumbnail of printed samples"></div><p>Lorem Ipsum simply dummy printing text<small>March , 21 2017</small></p></div>

  <div class="newsletter">
    <p>Lorem Ipsum is simply dummy text of the printing and typesetting industry. Lorem Ipsum has been the industry's.</p>
    <div class="email-box">Email<span class="email-go"><svg width="26" height="22" viewBox="0 0 26 22"><path d="M1 10L25 1l-6 20-6-7-5 5V13L21 4 6 12z" fill="#fff"/></svg></span></div>
    <div class="social"><span></span><span></span><span></span><span></span></div>
  </div>
</footer>

<div class="bottom-bar">
  <p>Copyright 2018 @ Gold Finch Print and Mailing Services</p>
  <div class="foot-brand">Gold Finch</div>
</div>

</body>
</html>
```